Summer Sale Graphics for Social Media

I want to create 11 social media graphics (new Instagram size 4:5 (1080 x 1350 pixels) focusing on our Summer Sale Graphics, using any of the pics attached. Use the attached pics, NO RANDOM STOCK PHOTOGRAPHY. For the color scheme of the graphics, they should all be complementary to the product colors in the photos.
You can add any of the photos attached but none are required. You can do some of the graphics in all text. I mainly need BOLD text that says one of the headlines (11 total) SEE ATTACHED WORD DOCUMENT for the headlines to use.

```html
<!DOCTYPE html>
<html lang="en">
<head>
<meta charset="utf-8">
<title>Summer Sale</title>
<link rel="stylesheet" href="https://fonts.googleapis.com/css2?family=Montserrat:wght@700&display=swap">
<style>
  :root {
    --sky: #1de0e0;
    --sky-deep: #22a8a8;
    --peach: #f8d2c6;
    --pink: #f24ba8;
    --magenta: #c63388;
    --palm: #1e8a50;
    --orange: #e04a1c;
    --white: #ffffff;
    --yellow: #f2da1e;
    --mint: #27e8c8;
    --green: #22f07a;
    --lilac: #c87af5;
    --amber: #f0b21e;
    --blue: #4a9bf0;
    --ocean: #1f77a0;
  }
  html, body { margin: 0; padding: 0; overflow: hidden; }
  .poster { width: 960px; height: 1200px; position: relative; overflow: hidden; background: var(--peach); }
  .poster svg { display: block; }
  .headline { font-family: "Montserrat", sans-serif; font-weight: 700; text-anchor: middle; }
</style>
</head>
<body>
<main class="poster">
  <svg width="960" height="1200" viewBox="0 0 960 1200">
    <g class="backdrop">
      <rect width="960" height="1200" fill="var(--peach)"/>
      <polygon class="band-sky" points="0,0 960,0 960,227 0,520" fill="var(--sky)"/>
      <polygon class="band-sky-stripe" points="0,307 578,0 960,0 960,36 0,329" fill="var(--sky-deep)"/>
      <polygon class="band-pink" points="204,1200 960,876 960,1200" fill="var(--pink)"/>
      <polygon class="band-magenta" points="622,1200 960,1013 960,1200" fill="var(--magenta)"/>
      <rect class="foliage-top" role="img" aria-label="Palm leaves at the top right corner"
        x="872" y="0" width="88" height="370" fill="var(--palm)"/>
      <rect class="foliage-bottom" role="img" aria-label="Palm leaves at the bottom left corner"
        x="0" y="812" width="88" height="388" fill="var(--palm)"/>
    </g>

    <g class="message-card">
      <rect x="116.5" y="133.5" width="713" height="700" fill="var(--orange)" stroke="var(--white)" stroke-width="9"/>
      <text class="headline" x="480" y="251" font-size="112" textLength="622" lengthAdjust="spacingAndGlyphs"><tspan fill="var(--white)">S</tspan><tspan fill="var(--yellow)">U</tspan><tspan fill="var(--mint)">M</tspan><tspan fill="var(--green)">M</tspan><tspan fill="var(--lilac)">E</tspan><tspan fill="var(--amber)">R</tspan><tspan fill="var(--yellow)">’</tspan><tspan fill="var(--blue)">S</tspan></text>
      <text class="headline" x="481" y="347" font-size="112" textLength="314" lengthAdjust="spacingAndGlyphs"><tspan fill="var(--green)">H</tspan><tspan fill="var(--white)">E</tspan><tspan fill="var(--yellow)">R</tspan><tspan fill="var(--mint)">E</tspan></text>
      <text class="headline" x="480" y="427" font-size="74" fill="var(--white)" textLength="455" lengthAdjust="spacingAndGlyphs">AND WE’RE</text>
      <text class="headline" x="483" y="502" font-size="74" fill="var(--white)" textLength="487" lengthAdjust="spacingAndGlyphs">HAVING THE</text>
      <text class="headline" x="479" y="613" font-size="105" fill="var(--mint)" textLength="486" lengthAdjust="spacingAndGlyphs">BIGGEST</text>
      <text class="headline" x="470" y="708" font-size="105" fill="var(--yellow)" textLength="286" lengthAdjust="spacingAndGlyphs">SALE</text>
      <text class="headline" x="473" y="794" font-size="74" fill="var(--white)" textLength="525" lengthAdjust="spacingAndGlyphs">OF THE YEAR</text>
    </g>

    <g class="cta">
      <rect x="126" y="873" width="694" height="211" fill="var(--peach)" stroke="var(--orange)" stroke-width="8"/>
      <text class="headline" x="481" y="1020" font-size="112" fill="var(--ocean)" textLength="616" lengthAdjust="spacingAndGlyphs">SALE NOW!</text>
    </g>
  </svg>
</main>
</body>
</html>
```